Business Card Professional Clean - Lumavault

Create a business card for my company that deals with Cryptocurrencies. I have a few designs ideas that I'd like to be implemented. Thanks! I will include the logo files, and a link to the design styles that I like.

Target Market(s)

Professionals

Industry/Entity Type

Consulting

Contact Information for Business Card

Name: Mark Dunn
Title: CEO/Technical Director
Phone: (587)943-0586
E-mail: mdunn@lumavault.ca
Address: Suite 512, 208-3370 Harwood Avenue NW

Twitter: @LumaVaultHQ
Instagram: lumavaulthq

Colors
92b5d7
3276b5
33a6d7
85acd3
85cae6
0592cd

Requirements
Must have
• Some colors that match with the logo and the pictures I put in below.
• Ideally the finished product would look something like the attachments showing the color gradient I want.
Nice to have
• Please see some of the attachments I've included. This is very close to the final product that I would like to see. If someone could recreate something like those I would definitely feel pretty good about it.
• For the instagram and twitter please use the symbols/icon to represent it on the card.
Should not have
• No crazy colors and unprofessional styles. I just want clear info. Don't go outside the boundaries of the colors in the attachment and we should be good. No crazy weird fonts either.

```html
<!DOCTYPE html>
<html lang="en">
<head>
<meta charset="utf-8">
<title>Lumavault Business Card</title>
<link rel="stylesheet" href="https://fonts.googleapis.com/css2?family=Roboto:wght@400;500&family=Roboto+Condensed:wght@500;700&display=swap">
<style>
  :root {
    --page-bg: #e9ebee;
    --brand-blue: #1b5fb8;
    --brand-blue-dark: #16509e;
    --brand-blue-light: #2a6fc4;
    --ink: #1d1d1f;
    --muted: #55585d;
    --divider: #3276b5;
    --card-white: #f7f7f6;
  }
  * { box-sizing: border-box; margin: 0; padding: 0; }
  html, body { width: 1200px; height: 886px; overflow: hidden; }
  body {
    background: var(--page-bg);
    font-family: "Roboto", Arial, sans-serif;
    position: relative;
  }
  .card {
    position: absolute;
    width: 560px;
    height: 320px;
    box-shadow: 0 10px 28px rgba(0,0,0,0.18);
  }
  /* Back side */
  .card-back {
    left: 60px;
    top: 80px;
    background: var(--brand-blue);
    overflow: hidden;
  }
  .card-back .pattern-area {
    position: absolute;
    inset: 0;
    background: linear-gradient(135deg, var(--brand-blue-light), var(--brand-blue) 55%, var(--brand-blue-dark));
  }
  .card-back .brand-lockup {
    position: absolute;
    right: 44px;
    top: 118px;
    display: flex;
    align-items: center;
    gap: 10px;
    color: #ffffff;
    font-size: 26px;
    font-weight: 500;
    letter-spacing: 0.5px;
  }
  .brand-mark-square {
    width: 18px;
    height: 18px;
    border: 3px solid currentColor;
  }
  .card-back .website {
    position: absolute;
    right: 44px;
    top: 176px;
    color: #ffffff;
    font-size: 13px;
    letter-spacing: 0.6px;
  }
  /* Front side */
  .card-front {
    left: 580px;
    top: 486px;
    background: var(--card-white);
  }
  .card-front .brand-lockup {
    position: absolute;
    right: 44px;
    top: 44px;
    display: flex;
    align-items: center;
    gap: 10px;
    color: var(--brand-blue);
    font-size: 30px;
    font-weight: 400;
    letter-spacing: 1px;
  }
  .person {
    position: absolute;
    left: 40px;
    top: 178px;
  }
  .person-name {
    font-family: "Roboto Condensed", "Arial Narrow", sans-serif;
    font-weight: 700;
    font-size: 21px;
    color: var(--brand-blue);
    line-height: 1;
  }
  .person-title {
    font-family: "Roboto Condensed", "Arial Narrow", sans-serif;
    font-weight: 700;
    font-size: 13px;
    color: var(--ink);
    margin-top: 3px;
    letter-spacing: 0.2px;
  }
  .contact-list {
    list-style: none;
    margin-top: 12px;
  }
  .contact-list li {
    display: flex;
    align-items: center;
    gap: 9px;
    font-size: 12.5px;
    color: var(--muted);
    line-height: 17px;
  }
  .contact-icon {
    width: 11px;
    height: 11px;
    flex: none;
    color: var(--brand-blue);
  }
  .social-square {
    width: 10px;
    height: 10px;
    background: var(--brand-blue);
    flex: none;
    margin: 0 1px 0 0;
  }
  .divider {
    position: absolute;
    left: 262px;
    top: 222px;
    width: 1px;
    height: 56px;
    background: var(--divider);
  }
  .address {
    position: absolute;
    left: 284px;
    top: 226px;
    font-size: 12.5px;
    color: var(--muted);
    line-height: 17px;
  }
</style>
</head>
<body>
  <section class="card card-back" aria-label="Business card back">
    <div class="pattern-area" role="img" aria-label="Repeating tonal blue brand pattern"></div>
    <div class="brand-lockup"><span class="brand-mark-square"></span><span>Lumavault</span></div>
    <div class="website">www.lumavault.ca</div>
  </section>

  <section class="card card-front" aria-label="Business card front">
    <div class="brand-lockup"><span class="brand-mark-square"></span><span>Lumavault</span></div>

    <div class="person">
      <div class="person-name">MARK DUNN</div>
      <div class="person-title">CEO/TECHNICAL DIRECTOR</div>
      <ul class="contact-list">
        <li>
          <svg class="contact-icon" viewBox="0 0 24 24" aria-hidden="true"><path fill="currentColor" d="M6.6 10.8a15.1 15.1 0 0 0 6.6 6.6l2.2-2.2c.3-.3.7-.4 1-.2 1.1.4 2.3.6 3.6.6.6 0 1 .4 1 1V20c0 .6-.4 1-1 1A17 17 0 0 1 3 4c0-.6.4-1 1-1h3.5c.6 0 1 .4 1 1 0 1.3.2 2.5.6 3.6.1.3 0 .7-.2 1z"/></svg>
          <span>(587)943-0586</span>
        </li>
        <li>
          <svg class="contact-icon" viewBox="0 0 24 24" aria-hidden="true"><path fill="currentColor" d="M2 5h20v14H2z"/><path d="M2 5l10 8 10-8" fill="none" stroke="#f7f7f6" stroke-width="2"/></svg>
          <span>mdunn@lumavault.ca</span>
        </li>
        <li><span class="social-square"></span><span>@LumaVaultHQ</span></li>
        <li><span class="social-square"></span><span>lumavaulthq</span></li>
      </ul>
    </div>

    <div class="divider"></div>
    <div class="address">Suite 512, 208-3370<br>Harwood Avenue NW</div>
  </section>
</body>
</html>
```